New Web Site - Professional Cleaning Company

I want to create a new attractive website that acts as an advertisement to visitors to entice them to reach out for more information.
We are a commercial/business janitorial service - with a new logo, would like the font to be complimentary to the font of logo, as well as the color scheme.
Target Market(s)
Commercial buildings, schools & medical buildings
Industry/Entity Type
Janitorial
Coding
Coded - Design and coding required
Number of Pages Required
4 page
Requirements
Must have
- Professionalism, sharp imagery

```html
<!DOCTYPE html>
<html lang="en">
<head>
<meta charset="utf-8">
<title>Brightwell Facility Services</title>
<link href="https://fonts.googleapis.com/css2?family=Poppins:wght@400;500;600;700;800&display=swap" rel="stylesheet">
<style>
:root{
  --navy:#17245e;
  --navy-deep:#0f1a47;
  --blue:#1f5fb0;
  --blue-mid:#2a76c9;
  --sky:#2b93d6;
  --ice:#e4f0fb;
  --ink:#3a3f4b;
  --white:#ffffff;
  --black:#0b0b0d;
  --gold:#f2b01e;
}
*{box-sizing:border-box;margin:0;padding:0}
html,body{width:1200px;height:4000px;overflow:hidden;background:var(--white)}
body{font-family:"Poppins",sans-serif;color:var(--ink)}
.page{position:relative;width:1200px;height:4000px;overflow:hidden;background:var(--white)}
.abs{position:absolute}
.btn{display:inline-block;background:var(--navy);color:var(--white);font-weight:600;font-size:15px;letter-spacing:.5px;padding:12px 30px;border-radius:30px;text-transform:uppercase}
.eyebrow{font-size:17px;font-weight:600;color:var(--navy);text-transform:uppercase;letter-spacing:1px}
.eyebrow.line::after{content:"";display:inline-block;width:60px;height:3px;background:var(--sky);vertical-align:middle;margin-left:14px}
.eyebrow.center{color:var(--white);text-align:center;width:100%}
.eyebrow.center::before,.eyebrow.center::after{content:"";display:inline-block;width:50px;height:2px;background:var(--white);vertical-align:middle;margin:0 16px}
.section-title{font-size:38px;font-weight:600;color:var(--sky);line-height:1.2}
.section-title.light{color:var(--white);text-align:center;width:100%}
.body-copy{font-size:16px;line-height:1.65;color:#555a66}
/* header */
.hero-photo{left:0;top:0;width:1200px;height:640px;background:linear-gradient(100deg,#2f4b5a 0%,#1d2f3c 40%,#3b3330 70%,#6b4a36 100%)}
.hero-shade{left:0;top:0;width:1200px;height:640px;background:linear-gradient(90deg,rgba(10,20,40,.1),rgba(10,20,40,.55))}
.brand{left:110px;top:8px;display:flex;align-items:center;gap:12px}
.brand-mark{width:130px;height:130px;border-radius:50%;background:var(--white);display:flex;align-items:center;justify-content:center;text-align:center;font-weight:700;font-size:15px;line-height:1.2;color:var(--navy);padding:14px}
.nav{left:290px;top:44px;display:flex;align-items:center;gap:30px;font-size:17px;color:var(--white)}
.nav a{color:var(--white);text-decoration:none}
.nav .current{border-bottom:3px solid var(--sky);padding-bottom:4px}
.nav .search{width:34px;height:34px;border-radius:50%;border:2px solid var(--white);display:flex;align-items:center;justify-content:center}
.nav .btn{background:var(--navy);border:2px solid var(--white);font-size:15px;padding:10px 22px}
.hero-copy{left:520px;top:240px;color:var(--white)}
.hero-copy .kicker{font-size:20px;font-weight:500;letter-spacing:1px;text-transform:uppercase}
.hero-copy h1{font-size:52px;font-weight:800;line-height:1.15;margin-top:14px;text-transform:uppercase}
.hero-copy .btn{margin-top:30px}
/* about */
.about{left:112px;top:760px;width:460px}
.about .section-title{margin:10px 0 22px}
.about .btn{margin-top:30px}
.photo-circle{border-radius:50%;border:10px solid var(--blue-mid)}
/* services */
.service-card{width:270px;height:290px;background:var(--ice);border-radius:14px;text-align:center;padding:100px 24px 0;box-shadow:0 8px 24px rgba(0,0,0,.18)}
.service-card h3{font-size:20px;font-weight:600;color:var(--navy);margin-bottom:8px}
.service-card h3::after{content:"";display:block;width:70px;height:2px;background:var(--sky);margin:10px auto 14px}
.service-card p{font-size:15px;line-height:1.55;color:#4a5060}
.service-icon{position:absolute;left:95px;top:-40px;width:80px;height:80px;border-radius:12px;background:var(--white);border:3px solid var(--sky);display:flex;align-items:center;justify-content:center}
.card-arrow{position:absolute;left:111px;bottom:-24px;width:48px;height:48px;border-radius:50%;background:var(--navy);display:flex;align-items:center;justify-content:center}
/* covid */
.covid{left:605px;top:2010px;width:540px}
.covid h2{margin:10px 0 10px}
.covid .sub{font-size:19px;font-weight:600;color:var(--navy);margin-bottom:16px}
.covid .btn{margin-top:30px}
/* reviews */
.review-card{width:440px;height:310px;background:var(--white);border-radius:12px;padding:46px 40px;box-shadow:0 8px 24px rgba(0,0,0,.2)}
.review-head{display:flex;align-items:center;gap:24px;margin-bottom:30px}
.avatar{width:84px;height:84px;border-radius:50%;border:4px solid var(--sky);background:linear-gradient(135deg,#5b7c8f,#2e4655)}
.reviewer{font-size:21px;font-weight:600;color:var(--navy)}
.stars{color:var(--gold);font-size:22px;letter-spacing:2px}
.dots{left:0;top:3050px;width:1200px;display:flex;justify-content:center;gap:10px}
.dots span{width:12px;height:12px;border-radius:50%;background:rgba(255,255,255,.5)}
.dots span.on{background:var(--white)}
/* contact */
.field{height:54px;border:1px solid #c8cdd6;border-radius:6px;font-size:15px;color:#8a8f9a;padding:16px 20px;background:var(--white)}
.contact-copy{left:632px;top:3240px;width:520px}
.contact-copy h2{margin:10px 0 14px;font-size:36px}
/* footer */
.footer{left:0;top:3560px;width:1200px;height:440px;background:var(--black);color:var(--white)}
.footer h4{font-size:16px;font-weight:700;text-transform:uppercase;letter-spacing:.5px;margin-bottom:18px}
.footer li{list-style:none;font-size:15px;line-height:1.9}
.footer-brand{left:470px;top:50px;width:260px;height:260px;border-radius:50%;border:2px solid #2a2a30;display:flex;align-items:center;justify-content:center;text-align:center;font-weight:700;font-size:22px;color:#3a3a44;padding:30px}
.contact-row{display:flex;gap:14px;align-items:flex-start;font-size:15px;line-height:1.5;margin-bottom:14px}
.copyright{left:0;top:390px;width:1200px;text-align:center;font-size:14px;color:#cfd2d8;border-top:1px solid #222;padding-top:14px}
</style>
</head>
<body>
<div class="page">

  <!-- Header / hero -->
  <div class="abs hero-photo" role="img" aria-label="Cleaner in protective mask and gloves wiping a window in an office"></div>
  <div class="abs hero-shade"></div>
  <svg class="abs" style="left:0;top:470px" width="1200" height="220" viewBox="0 0 1200 220">
    <path d="M0 110 C250 40 520 190 820 120 C980 85 1100 60 1200 70 V220 H0Z" fill="var(--white)"/>
    <path d="M700 150 C850 120 980 80 1200 60 V82 C1000 100 880 135 700 150Z" fill="var(--navy)"/>
    <path d="M0 150 C120 130 240 150 330 175 C230 165 120 160 0 170Z" fill="var(--navy)"/>
  </svg>
  <div class="abs brand"><div class="brand-mark">Brightwell Facility Services</div></div>
  <nav class="abs nav">
    <a class="current">Home</a><a>About</a><a>Services</a><a>COVID-19</a><a>Reviews</a><a>Blog</a><a>Contact</a>
    <span class="search"><svg width="16" height="16" viewBox="0 0 16 16"><circle cx="7" cy="7" r="5" fill="none" stroke="#fff" stroke-width="2"/><line x1="11" y1="11" x2="15" y2="15" stroke="#fff" stroke-width="2"/></svg></span>
    <span class="btn">Get a Quote</span>
  </nav>
  <div class="abs hero-copy">
    <div class="kicker">Brightwell Facility Services</div>
    <h1>The Fine Experience<br>of Cleaning</h1>
    <span class="btn">Get a Quote</span>
  </div>

  <!-- About -->
  <section class="abs about">
    <div class="eyebrow line">About</div>
    <h2 class="section-title">Brightwell Facility Services</h2>
    <p class="body-copy">Sed ut perspiciatis unde omnis iste natus error voluptatem accusantium doloremque laudantium, totam rem aperiam, eaque ipsa quae ab illo inventore veritatis et quasi architec beatae vitae dicta sunt explicabo. Nemo enim ipsam volupt quia voluptas sit aspernatur aut odit aut fugi.</p>
    <span class="btn">Learn More</span>
  </section>
  <div class="abs photo-circle" style="left:700px;top:700px;width:290px;height:290px;background:linear-gradient(140deg,#cfe3f3,#8fb7d9 55%,#2c4f8a)" role="img" aria-label="Cleaner in a cap spraying and wiping a window"></div>

  <!-- Services band -->
  <svg class="abs" style="left:0;top:1100px" width="1200" height="820" viewBox="0 0 1200 820">
    <defs><linearGradient id="bandA" x1="0" y1="0" x2="1" y2="1"><stop offset="0" stop-color="#1d4f9c"/><stop offset=".5" stop-color="#2a76c9"/><stop offset="1" stop-color="#1a4a92"/></linearGradient></defs>
    <path d="M0 60 C300 140 600 0 900 40 C1030 58 1120 90 1200 80 V720 C950 800 700 700 400 730 C250 745 120 780 0 760Z" fill="url(#bandA)"/>
    <path d="M0 740 C200 730 330 760 460 800 C320 780 150 770 0 790Z" fill="var(--navy)"/>
    <path d="M850 760 C980 720 1100 700 1200 690 V715 C1090 725 980 745 850 760Z" fill="var(--navy)"/>
  </svg>
  <div class="abs eyebrow center" style="left:0;top:1290px">Services</div>
  <h2 class="abs section-title light" style="left:0;top:1325px;font-size:36px">Brightwell Facility Services</h2>

  <div class="abs service-card" style="left:130px;top:1460px">
    <div class="service-icon"><svg width="48" height="48" viewBox="0 0 48 48"><rect x="6" y="10" width="16" height="34" fill="#2fb36b"/><rect x="24" y="4" width="18" height="40" fill="#2fb36b"/><g fill="#fff"><rect x="10" y="16" width="4" height="4"/><rect x="10" y="24" width="4" height="4"/><rect x="28" y="10" width="4" height="4"/><rect x="34" y="10" width="4" height="4"/><rect x="28" y="18" width="4" height="4"/><rect x="34" y="18" width="4" height="4"/></g></svg></div>
    <h3>Commercial buildings</h3>
    <p>Ut enim ad minima veniam, quis nostrum exercitation.</p>
    <div class="card-arrow"><svg width="20" height="14" viewBox="0 0 20 14"><path d="M0 7H17M12 2L17 7L12 12" stroke="#fff" stroke-width="2" fill="none"/></svg></div>
  </div>
  <div class="abs service-card" style="left:465px;top:1460px">
    <div class="service-icon"><svg width="48" height="48" viewBox="0 0 48 48"><path d="M4 20L24 8L44 20V44H4Z" fill="#2fb36b"/><rect x="20" y="30" width="8" height="14" fill="#fff"/><circle cx="24" cy="20" r="4" fill="#fff"/></svg></div>
    <h3>Schools</h3>
    <p>Ut enim ad minima veniam, quis nostrum exercitation.</p>
    <div class="card-arrow"><svg width="20" height="14" viewBox="0 0 20 14"><path d="M0 7H17M12 2L17 7L12 12" stroke="#fff" stroke-width="2" fill="none"/></svg></div>
  </div>
  <div class="abs service-card" style="left:800px;top:1460px">
    <div class="service-icon"><svg width="48" height="48" viewBox="0 0 48 48"><rect x="6" y="12" width="36" height="32" fill="#2fb36b"/><path d="M21 16H27V22H33V28H27V34H21V28H15V22H21Z" fill="#fff"/></svg></div>
    <h3>Medical buildings</h3>
    <p>Ut enim ad minima veniam, quis nostrum exercitation.</p>
    <div class="card-arrow"><svg width="20" height="14" viewBox="0 0 20 14"><path d="M0 7H17M12 2L17 7L12 12" stroke="#fff" stroke-width="2" fill="none"/></svg></div>
  </div>

  <!-- COVID -->
  <div class="abs photo-circle" style="left:120px;top:2020px;width:390px;height:390px;background:linear-gradient(135deg,#e8eef3,#a9bccb 50%,#3c5a78)" role="img" aria-label="Worker in protective suit disinfecting an office"></div>
  <section class="abs covid">
    <div class="eyebrow">COVID 19</div>
    <h2 class="section-title">Response To Pandemic</h2>
    <div class="sub">Disinfectant Treatment During COVID-19.</div>
    <p class="body-copy">Sed ut perspiciatis unde omnis iste natus error voluptatem accusantium doloremque laudantium, totam rem aperiam, eaque ipsa quae ab illo inventore veritatis et quasi architec beatae vitae dicta sunt explicabo. Nemo enim ipsam volupt quia voluptas sit aspernatur aut odit aut fugi.</p>
    <span class="btn">Learn More</span>
  </section>

  <!-- Reviews band -->
  <svg class="abs" style="left:0;top:2480px" width="1200" height="760" viewBox="0 0 1200 760">
    <defs><linearGradient id="bandB" x1="0" y1="0" x2="1" y2="1"><stop offset="0" stop-color="#1d4f9c"/><stop offset=".5" stop-color="#2a76c9"/><stop offset="1" stop-color="#1a4a92"/></linearGradient></defs>
    <path d="M0 90 C250 20 520 110 800 70 C960 48 1100 20 1200 40 V660 C1000 700 800 640 560 690 C360 730 160 700 0 720Z" fill="url(#bandB)"/>
    <path d="M0 70 C150 50 300 60 420 90 C280 75 140 75 0 95Z" fill="var(--navy)"/>
    <path d="M820 700 C960 660 1090 640 1200 630 V655 C1080 668 960 690 820 700Z" fill="var(--navy)"/>
  </svg>
  <div class="abs eyebrow center" style="left:0;top:2610px">Reviews</div>
  <h2 class="abs section-title light" style="left:0;top:2645px;font-size:36px">What Our Client Say</h2>
  <div class="abs review-card" style="left:100px;top:2728px">
    <div class="review-head"><div class="avatar" role="img" aria-label="Client portrait"></div><div><div class="reviewer">Mara Ellison</div><div class="stars">★★★★★</div></div></div>
    <p class="body-copy">Nam libero tempore, cum soluta nobiseligen optio cumque nihil impedit quominus iquod maxime placeat facere.</p>
  </div>
  <div class="abs review-card" style="left:640px;top:2728px">
    <div class="review-head"><div class="avatar" role="img" aria-label="Client portrait"></div><div><div class="reviewer">Mara Ellison</div><div class="stars">★★★★★</div></div></div>
    <p class="body-copy">Nam libero tempore, cum soluta nobiseligen optio cumque nihil impedit quominus iquod maxime placeat facere.</p>
  </div>
  <div class="abs dots"><span class="on"></span><span></span><span></span><span></span></div>

  <!-- Contact -->
  <div class="abs field" style="left:112px;top:3280px;width:220px">Name</div>
  <div class="abs field" style="left:350px;top:3280px;width:230px">Email</div>
  <div class="abs field" style="left:112px;top:3352px;width:468px">Choose your service
    <svg style="position:absolute;right:18px;top:22px" width="14" height="10" viewBox="0 0 14 10"><path d="M1 1L7 8L13 1" stroke="#555" stroke-width="2" fill="none"/></svg></div>
  <span class="abs btn" style="left:112px;top:3430px">Get a Quote</span>
  <section class="abs contact-copy">
    <div class="eyebrow line">Get in Touch</div>
    <h2 class="section-title">Find Standard Cleaning with Personal Touch</h2>
    <p class="body-copy">At vero eos et accusamus et iusto odio dignis ducimusu blanditiis praesentium voluptatum deleniti.</p>
  </section>

  <!-- Footer -->
  <footer class="abs footer">
    <div class="abs" style="left:112px;top:70px">
      <h4>Quick Links</h4>
      <div style="display:flex;gap:80px">
        <ul><li>Home</li><li>About</li><li>Services</li><li>COVID-19</li></ul>
        <ul><li>Reviews</li><li>Blog</li><li>Contact</li></ul>
      </div>
    </div>
    <div class="abs footer-brand">Brightwell Facility Services</div>
    <div class="abs" style="left:860px;top:70px;width:300px">
      <h4>Contact Us</h4>
      <div class="contact-row"><svg width="16" height="20" viewBox="0 0 16 20"><path d="M8 0C3.6 0 0 3.4 0 7.6 0 13 8 20 8 20S16 13 16 7.6C16 3.4 12.4 0 8 0Z" fill="#fff"/><circle cx="8" cy="7.5" r="3" fill="#0b0b0d"/></svg><span>Brightwell Facility Services,<br>Address Here</span></div>
      <div class="contact-row"><svg width="18" height="18" viewBox="0 0 18 18"><path d="M4 1L7 5 5 7C6 10 8 12 11 13L13 11 17 14 15 17C8 17 1 10 1 3Z" fill="#fff"/></svg><span>+1 555-010-2040</span></div>
      <div class="contact-row"><svg width="18" height="14" viewBox="0 0 18 14"><rect x="0" y="0" width="18" height="14" rx="2" fill="#fff"/><path d="M1 1L9 8 17 1" stroke="#0b0b0d" stroke-width="1.5" fill="none"/></svg><span>info@brightwellfacility.com</span></div>
    </div>
    <div class="abs copyright">2022 Brightwell Facility Services. All Rights Reserved.</div>
  </footer>

</div>
</body>
</html>
```